New Business Card

Use website for color, logo and theme.

http://www.plumwickonline.com/

Back side of card should be programs listed on home page of website

1) Phone Number is (800) 555-0142 x23
2) Fax (240) 555-0187
3) Address is - 647 W Harlowe Street, Suite 312, Baltimore, MD 21201
4) NMLS #738516

```html
<!DOCTYPE html>
<html lang="en">
<head>
<meta charset="utf-8">
<title>Plumwick Financial Services – Business Card</title>
<link href="https://fonts.googleapis.com/css2?family=Open+Sans:wght@400;600;700&display=swap" rel="stylesheet">
<style>
  :root {
    --page: #ecebe6;
    --card: #ffffff;
    --gold: #a89a3a;
    --gold-light: #bcae4e;
    --gold-dark: #857824;
    --blue: #2a64ab;
    --navy: #1d4785;
    --photo: #6d6e73;
    --white: #ffffff;
  }
  * { margin: 0; padding: 0; box-sizing: border-box; }
  html, body {
    width: 1200px; height: 913px; overflow: hidden;
    background: var(--page);
    font-family: "Open Sans", Arial, sans-serif;
  }
  .card {
    position: absolute;
    width: 600px; height: 343px;
    background: var(--card);
    border-radius: 18px;
    overflow: hidden;
    box-shadow: 0 6px 18px rgba(0,0,0,.18);
  }
  .card-front { left: 60px; top: 70px; }
  .card-back { left: 540px; top: 500px; }

  .front-band { position: absolute; inset: 0; width: 100%; height: 100%; }

  .brand {
    position: absolute; display: flex; align-items: center; gap: 10px;
    color: var(--gold); font-weight: 700; font-size: 15px; line-height: 1.2;
  }
  .brand-dot { width: 18px; height: 18px; border-radius: 50%; background: var(--blue); flex: none; }
  .card-front .brand { left: 30px; top: 146px; width: 200px; }

  .portrait {
    position: absolute; right: 36px; top: 18px;
    width: 184px; height: 108px;
    border: 2px solid var(--blue); padding: 4px; background: var(--white);
  }
  .portrait-fill { width: 100%; height: 100%; background: linear-gradient(135deg, #8a8c90, var(--photo) 60%, #3f4045); }

  .address {
    position: absolute; right: 36px; top: 132px;
    text-align: right; color: var(--gold); font-size: 13px; line-height: 1.35;
  }

  .contact {
    position: absolute; left: 150px; top: 220px; color: var(--white);
  }
  .contact-name { font-size: 24px; font-weight: 700; line-height: 1.1; }
  .contact-role { font-size: 15px; color: var(--blue); font-weight: 600; line-height: 1.3; }
  .contact-id { font-size: 13px; line-height: 1.35; margin-bottom: 2px; }
  .contact-line { display: flex; align-items: center; gap: 8px; font-size: 14px; line-height: 1.3; }
  .contact-line svg { width: 12px; height: 12px; flex: none; }

  .card-back .brand {
    left: 50%; top: 56px; transform: translateX(-50%);
    font-size: 20px; white-space: nowrap;
  }
  .back-rule {
    position: absolute; left: 110px; right: 110px; top: 128px;
    height: 1px; background: linear-gradient(90deg, transparent, var(--blue), transparent);
  }
  .headline {
    position: absolute; left: 0; right: 0; top: 146px;
    text-align: center; color: var(--gold); font-weight: 700; font-size: 17px; line-height: 1.25;
  }
  .programs {
    position: absolute; left: 0; right: 0; top: 212px;
    list-style: none; text-align: center; color: var(--gold); font-size: 17px; line-height: 1.5;
  }
  .programs li { display: inline-flex; align-items: center; gap: 7px; margin: 0 8px; }
  .programs li::before {
    content: ""; width: 11px; height: 11px; border-radius: 50%; background: var(--navy);
  }
  .programs li:nth-child(2)::before { background: var(--blue); }
  .programs li:nth-child(3)::before { background: #3e79c1; }
</style>
</head>
<body>

<section class="card card-front" aria-label="Card front">
  <svg class="front-band" viewBox="0 0 600 343" preserveAspectRatio="none">
    <defs>
      <linearGradient id="goldFill" x1="0" y1="0" x2="1" y2="1">
        <stop offset="0" stop-color="#bcae4e"/>
        <stop offset="1" stop-color="#857824"/>
      </linearGradient>
    </defs>
    <path d="M140 218 C300 186 450 176 600 178 L600 200 C420 198 260 205 110 228 Z" fill="var(--blue)"/>
    <path d="M0 242 C160 212 380 196 600 198 L600 343 L0 343 Z" fill="url(#goldFill)"/>
  </svg>

  <div class="brand"><span class="brand-dot"></span><span>Plumwick Financial<br>Services, Inc.</span></div>

  <div class="portrait"><div class="portrait-fill" role="img" aria-label="Portrait photo of the loan officer"></div></div>

  <p class="address">647 W Harlowe Street<br>Suite 312, Baltimore, MD 21201</p>

  <div class="contact">
    <p class="contact-name">Dale Marrow</p>
    <p class="contact-role">Owner</p>
    <p class="contact-id">NMLS #738516</p>
    <p class="contact-line">
      <svg viewBox="0 0 12 12"><rect x="1" y="3" width="10" height="7" rx="1" fill="var(--blue)"/><rect x="3" y="1" width="6" height="3" fill="var(--blue)"/></svg>
      (240) 555-0187
    </p>
    <p class="contact-line">
      <svg viewBox="0 0 12 12"><path d="M3 1 L5 3.5 L4 5 C5 7 6 8 7 8.5 L8.5 7.5 L11 9.5 L9.5 11 C5 11 1 7 1 2.5 Z" fill="var(--blue)"/></svg>
      (800) 555-0142 x23
    </p>
    <p class="contact-line">
      <svg viewBox="0 0 12 12"><circle cx="6" cy="6" r="5" fill="var(--blue)"/><path d="M1 6 H11 M6 1 C3.5 4 3.5 8 6 11 M6 1 C8.5 4 8.5 8 6 11" stroke="#fff" stroke-width=".8" fill="none"/></svg>
      www.plumwickonline.com
    </p>
  </div>
</section>

<section class="card card-back" aria-label="Card back">
  <div class="brand"><span class="brand-dot"></span><span>Plumwick Financial Services, Inc.</span></div>
  <div class="back-rule"></div>
  <p class="headline">CHECK OUT OUR<br>EXCITING NEW PRODUCT LINE</p>
  <ul class="programs">
    <li>Traditional Loan Programs</li>
    <li>Low Credit Score Programs</li>
    <li>Alternative Loan Programs</li>
  </ul>
</section>

</body>
</html>
```